Thriller/Romance novel book cover design - Eight Grey Gulls

I need a book cover for a novel (print + ebook). Genre = thriller / romance. Title = Eight Grey Gulls. Author = Dorian Felt.
Story is set in Caribbean. 45-year-old Ex-NVB agent is hunted by corrupt politicians, NVB and cartel. He is a life-long fisherman and seaman who joined the Army after college and became a war hero, followed by 10 years as operative for the NVB. Betrayal from Washington saw him accused of killing his mentor/friend/NVB Director and he is now a fugitive. He has been hiding for 7 years on Grand Cayman, and lives a secluded, private life as a fisherman on his modern sportfisherman-style boat ('50 Quellmoor Runabout for reference). Boat name = Eight Grey Gulls (as in the playing card) represents fate to him and his high school sweetheart to whom he was engaged before a tragic event separated them. His main goal, beyond survival, is to reunite with his long, lost love, but he can't risk putting her in danger until he settles the case and those searching for him. The boat name (Eight Grey Gulls) only has relevance to him and his soulmate, who is not even aware that he is still alive.

Target Market(s)

thriller and romantic thriller readers

Requirements
Must have
• author name should be small on bottom of cover - not at top. Design is wide open for creative ideas. If a boat is used in artwork, it must be a modern sportfisherman style boat (zintrope will define this
Nice to have
• I like intrigue and mystery. Don't try to explain or show too much. Prefer sunsets (orange, red, purple, yellow) to blue sky, blue water to give it a darker tone
Should not have
• do not want images of people on the cover like many romance novels do.

```html
<!DOCTYPE html>
<html lang="en">
<head>
<meta charset="utf-8">
<title>Eight Grey Gulls — Dorian Felt</title>
<link rel="stylesheet" href="https://fonts.googleapis.com/css2?family=Abril+Fatface&family=Open+Sans:wght@700&display=swap">
<style>
  :root {
    --backdrop: #e4e5e6;
    --sky-top: #5d6a70;
    --sky-slate: #4a4858;
    --sky-violet: #7a4656;
    --sky-red: #d8452c;
    --sky-orange: #ef6a2a;
    --horizon-gold: #f8c040;
    --sea-glow: #d2522a;
    --sea-red: #7e2a24;
    --sea-navy: #2c3248;
    --sea-deep: #161c2a;
    --title-white: #ffffff;
    --title-yellow: #ffe01a;
    --title-shadow: #111111;
    --card-paper: #efe9dd;
    --card-worn: #cfc3aa;
    --card-edge: #8a7456;
  }
  * { margin: 0; padding: 0; box-sizing: border-box; }
  html, body {
    width: 1200px; height: 1200px; overflow: hidden;
    background: var(--backdrop);
  }
  .cover {
    position: absolute;
    left: 188px; top: 41px;
    width: 824px; height: 1098px;
    overflow: hidden;
  }
  .sky-art {
    position: absolute; left: 0; top: 0; width: 100%; height: 614px;
    background:
      radial-gradient(ellipse 420px 150px at 10% 100%, rgba(248,192,64,0.95), rgba(248,192,64,0) 100%),
      radial-gradient(ellipse 500px 200px at 85% 20%, rgba(40,40,60,0.55), rgba(40,40,60,0) 100%),
      linear-gradient(180deg,
        var(--sky-top) 0%,
        var(--sky-slate) 14%,
        var(--sky-violet) 28%,
        var(--sky-red) 48%,
        var(--sky-orange) 80%,
        #f38a36 100%);
  }
  .sea-art {
    position: absolute; left: 0; top: 614px; width: 100%; bottom: 0;
    background:
      radial-gradient(ellipse 360px 120px at 12% 0%, rgba(240,120,40,0.8), rgba(240,120,40,0) 100%),
      linear-gradient(180deg,
        var(--sea-glow) 0%,
        var(--sea-red) 22%,
        var(--sea-navy) 55%,
        var(--sea-deep) 100%);
  }
  .card-art {
    position: absolute;
    left: 258px; top: 401px;
    width: 300px; height: 410px;
    border-radius: 12px;
    background:
      radial-gradient(ellipse at 50% 45%, var(--card-paper) 50%, var(--card-worn) 85%, var(--card-edge) 100%);
    box-shadow: inset 0 0 0 3px rgba(120,95,65,0.45), 0 8px 20px rgba(0,0,0,0.4);
    transform: rotate(4deg);
  }
  .title {
    position: absolute; left: 0; right: 0; top: 40px;
    text-align: center;
    font-family: "Abril Fatface", serif;
    text-transform: uppercase;
    line-height: 0.9;
  }
  .title-line {
    display: block;
    text-shadow: 8px 6px 0 var(--title-shadow);
  }
  .title-line--first { color: var(--title-white); font-size: 180px; letter-spacing: 2px; }
  .title-line--second { color: var(--title-yellow); font-size: 132px; letter-spacing: 0; margin-top: 4px; }
  .author {
    position: absolute; left: 0; right: 0; bottom: 46px;
    text-align: center;
    font-family: "Open Sans", sans-serif;
    font-weight: 700;
    font-size: 58px;
    letter-spacing: -1px;
    color: var(--title-white);
    text-shadow: 4px 3px 0 var(--title-shadow);
  }
</style>
</head>
<body>
  <main class="cover">
    <div class="sky-art" role="img" aria-label="Photograph of a fiery Caribbean sunset sky with a palm-lined island silhouette on the left horizon"></div>
    <div class="sea-art" role="img" aria-label="Photograph of dark open sea reflecting the orange sunset"></div>
    <div class="card-art" role="img" aria-label="Weathered playing card standing upright in the sea, pierced by a bullet hole"></div>
    <h1 class="title">
      <span class="title-line title-line--first">Eight</span>
      <span class="title-line title-line--second">Grey Gulls</span>
    </h1>
    <p class="author">Dorian Felt</p>
  </main>
</body>
</html>
```